Hops, Riffs & Sunset Grillout.

I need an A3 Poster, Insta Square and Facebook Event Cover photo for a Hops Riffs and Grill Event. Details as follows:

Name: Hops, Riffs and Sunset Grill
12pm - Late. Jan 26th at Copperleaf Yard Brewhouse
Acts:
Blue Tern - 7pm
Velvet Kite & Slow Morris - 3pm - 7pm
Grant Whitcombe - 12pm -3pm

Free BBQ 2-4pm.

```html
<!DOCTYPE html>
<html lang="en">
<head>
<meta charset="utf-8">
<title>Hops, Riffs &amp; Sunset Grill – Event Set</title>
<link href="https://fonts.googleapis.com/css2?family=Oswald:wght@400;500;600&display=swap" rel="stylesheet">
<style>
  :root{
    --backdrop:#e8e8e6;
    --paper:#ffffff;
    --ink:#1d2b3a;
    --accent:#6e3b36;
    --art-light:#dfe4ea;
    --art-dark:#9aa6b4;
    --shadow:rgba(0,0,0,.12);
  }
  *{margin:0;padding:0;box-sizing:border-box}
  html,body{width:1099px;height:1200px;overflow:hidden;background:var(--backdrop)}
  body{position:relative;font-family:'Oswald',sans-serif;color:var(--ink)}

  .piece{position:absolute;background:var(--paper);box-shadow:0 14px 10px -10px var(--shadow)}
  .cover{left:130px;top:121px;width:839px;height:311px}
  .poster{left:130px;top:486px;width:401px;height:567px}
  .square{left:564px;top:486px;width:405px;height:405px}

  .emblem{position:absolute;display:block;overflow:visible}
  .emblem-title{font-family:'Oswald',sans-serif;font-weight:600;font-size:44px;fill:var(--ink);letter-spacing:2px;text-transform:uppercase}
  .cover .emblem{left:73px;top:24px;width:250px;height:250px}
  .poster .emblem{left:45px;top:28px;width:315px;height:315px}
  .square .emblem{left:90px;top:16px;width:225px;height:225px}

  .divider{position:absolute;width:1px;background:var(--ink)}
  .cover .divider{left:365px;top:26px;height:258px}
  .poster .divider{left:184px;top:465px;height:76px}
  .square .divider{left:187px;top:316px;height:73px}

  .venue-name{position:absolute;font-weight:600;color:var(--ink);text-transform:uppercase;line-height:1.05;text-align:center}
  .cover .venue-name{left:519px;top:22px;width:149px;font-size:17px}
  .poster .venue-name{left:30px;top:478px;width:136px;font-size:17px}
  .square .venue-name{left:30px;top:326px;width:130px;font-size:16px}

  .details{position:absolute;text-align:center}
  .cover .details{left:594px;top:104px;transform:translateX(-50%);width:300px}
  .poster .details{left:208px;top:462px;width:161px}
  .square .details{left:214px;top:313px;width:152px}

  .when{font-weight:400;line-height:1.1;white-space:nowrap}
  .cover .when{font-size:44px}
  .poster .when{font-size:21px}
  .square .when{font-size:20px}

  .where{display:flex;align-items:center;gap:10px;white-space:nowrap}
  .where::before,.where::after{content:"";flex:1;height:1px;background:var(--ink)}
  .cover .where{font-size:18px;margin-top:2px;gap:14px}
  .poster .where,.square .where{font-size:8.5px;gap:6px}

  .acts{display:flex;align-items:center;text-align:left}
  .cover .acts{margin-top:14px;gap:14px}
  .poster .acts{margin-top:10px;gap:7px}
  .square .acts{margin-top:8px;gap:7px}
  .acts-label{white-space:nowrap}
  .cover .acts-label{font-size:26px}
  .poster .acts-label,.square .acts-label{font-size:12px}
  .act-list{list-style:none}
  .act{display:flex;align-items:center;white-space:nowrap}
  .cover .act{font-size:16.5px;height:22px;gap:7px}
  .poster .act{font-size:8px;height:12px;gap:4px}
  .square .act{font-size:7.5px;height:11.5px;gap:4px}
  .note{fill:none;stroke:var(--ink);stroke-width:1.2}
  .cover .note{width:17px;height:13px}
  .poster .note,.square .note{width:9px;height:7px}

  .free-bbq{position:absolute;color:var(--accent);font-weight:400;white-space:nowrap;transform:translateX(-50%)}
  .cover .free-bbq{left:594px;top:272px;font-size:19px;line-height:1}
  .poster .free-bbq{left:201px;top:395px;font-size:29px}
  .square .free-bbq{left:202px;top:276px;font-size:19px}
</style>
</head>
<body>

<!-- Facebook event cover -->
<section class="piece cover">
  <svg class="emblem" viewBox="0 0 300 300" aria-label="Hops, Riffs &amp; Sunset Grill">
    <defs>
      <path id="arc-top-c" d="M 38 150 A 112 112 0 0 1 262 150"/>
      <path id="arc-bot-c" d="M 10 150 A 140 140 0 0 0 290 150"/>
      <radialGradient id="art-c"><stop offset="0" stop-color="var(--art-light)"/><stop offset="1" stop-color="var(--art-dark)"/></radialGradient>
    </defs>
    <circle cx="150" cy="150" r="90" fill="url(#art-c)" role="img" aria-label="Line illustration of a beer stein, guitar, speaker, microphone, grill and sausage"/>
    <text class="emblem-title"><textPath href="#arc-top-c" startOffset="50%" text-anchor="middle">Hops, Riffs</textPath></text>
    <text class="emblem-title"><textPath href="#arc-bot-c" startOffset="50%" text-anchor="middle">&amp; Sunset Grill</textPath></text>
  </svg>
  <div class="divider"></div>
  <div class="venue-name">Copperleaf Yard Brewhouse</div>
  <div class="details">
    <p class="when">12pm - Late. Jan 26th</p>
    <p class="where">at Copperleaf Yard Brewhouse</p>
    <div class="acts">
      <span class="acts-label">ACTS:</span>
      <ul class="act-list">
        <li class="act"><svg class="note" viewBox="0 0 14 11"><path d="M5 9V2l8-1.5V7.5M5 3.5l8-1.5"/><ellipse cx="3" cy="9" rx="2" ry="1.5"/><ellipse cx="11" cy="7.5" rx="2" ry="1.5"/></svg>Blue Tern - 7pm</li>
        <li class="act"><svg class="note" viewBox="0 0 14 11"><path d="M5 9V2l8-1.5V7.5M5 3.5l8-1.5"/><ellipse cx="3" cy="9" rx="2" ry="1.5"/><ellipse cx="11" cy="7.5" rx="2" ry="1.5"/></svg>Velvet Kite &amp; Slow Morris - 3pm - 7pm</li>
        <li class="act"><svg class="note" viewBox="0 0 14 11"><path d="M5 9V2l8-1.5V7.5M5 3.5l8-1.5"/><ellipse cx="3" cy="9" rx="2" ry="1.5"/><ellipse cx="11" cy="7.5" rx="2" ry="1.5"/></svg>Grant Whitcombe - 12pm - 3pm</li>
      </ul>
    </div>
  </div>
  <p class="free-bbq">Free BBQ 2-4pm</p>
</section>

<!-- A3 poster -->
<section class="piece poster">
  <svg class="emblem" viewBox="0 0 300 300" aria-label="Hops, Riffs &amp; Sunset Grill">
    <defs>
      <path id="arc-top-p" d="M 38 150 A 112 112 0 0 1 262 150"/>
      <path id="arc-bot-p" d="M 10 150 A 140 140 0 0 0 290 150"/>
      <radialGradient id="art-p"><stop offset="0" stop-color="var(--art-light)"/><stop offset="1" stop-color="var(--art-dark)"/></radialGradient>
    </defs>
    <circle cx="150" cy="150" r="90" fill="url(#art-p)" role="img" aria-label="Line illustration of a beer stein, guitar, speaker, microphone, grill and sausage"/>
    <text class="emblem-title"><textPath href="#arc-top-p" startOffset="50%" text-anchor="middle">Hops, Riffs</textPath></text>
    <text class="emblem-title"><textPath href="#arc-bot-p" startOffset="50%" text-anchor="middle">&amp; Sunset Grill</textPath></text>
  </svg>
  <p class="free-bbq">Free BBQ 2-4pm</p>
  <div class="venue-name">Copperleaf Yard Brewhouse</div>
  <div class="divider"></div>
  <div class="details">
    <p class="when">12pm - Late. Jan 26th</p>
    <p class="where">at Copperleaf Yard Brewhouse</p>
    <div class="acts">
      <span class="acts-label">ACTS:</span>
      <ul class="act-list">
        <li class="act"><svg class="note" viewBox="0 0 14 11"><path d="M5 9V2l8-1.5V7.5M5 3.5l8-1.5"/><ellipse cx="3" cy="9" rx="2" ry="1.5"/><ellipse cx="11" cy="7.5" rx="2" ry="1.5"/></svg>Blue Tern - 7pm</li>
        <li class="act"><svg class="note" viewBox="0 0 14 11"><path d="M5 9V2l8-1.5V7.5M5 3.5l8-1.5"/><ellipse cx="3" cy="9" rx="2" ry="1.5"/><ellipse cx="11" cy="7.5" rx="2" ry="1.5"/></svg>Velvet Kite &amp; Slow Morris - 3pm - 7pm</li>
        <li class="act"><svg class="note" viewBox="0 0 14 11"><path d="M5 9V2l8-1.5V7.5M5 3.5l8-1.5"/><ellipse cx="3" cy="9" rx="2" ry="1.5"/><ellipse cx="11" cy="7.5" rx="2" ry="1.5"/></svg>Grant Whitcombe - 12pm - 3pm</li>
      </ul>
    </div>
  </div>
</section>

<!-- Instagram square -->
<section class="piece square">
  <svg class="emblem" viewBox="0 0 300 300" aria-label="Hops, Riffs &amp; Sunset Grill">
    <defs>
      <path id="arc-top-s" d="M 38 150 A 112 112 0 0 1 262 150"/>
      <path id="arc-bot-s" d="M 10 150 A 140 140 0 0 0 290 150"/>
      <radialGradient id="art-s"><stop offset="0" stop-color="var(--art-light)"/><stop offset="1" stop-color="var(--art-dark)"/></radialGradient>
    </defs>
    <circle cx="150" cy="150" r="90" fill="url(#art-s)" role="img" aria-label="Line illustration of a beer stein, guitar, speaker, microphone, grill and sausage"/>
    <text class="emblem-title"><textPath href="#arc-top-s" startOffset="50%" text-anchor="middle">Hops, Riffs</textPath></text>
    <text class="emblem-title"><textPath href="#arc-bot-s" startOffset="50%" text-anchor="middle">&amp; Sunset Grill</textPath></text>
  </svg>
  <p class="free-bbq">Free BBQ 2-4pm</p>
  <div class="venue-name">Copperleaf Yard Brewhouse</div>
  <div class="divider"></div>
  <div class="details">
    <p class="when">12pm - Late. Jan 26th</p>
    <p class="where">at Copperleaf Yard Brewhouse</p>
    <div class="acts">
      <span class="acts-label">ACTS:</span>
      <ul class="act-list">
        <li class="act"><svg class="note" viewBox="0 0 14 11"><path d="M5 9V2l8-1.5V7.5M5 3.5l8-1.5"/><ellipse cx="3" cy="9" rx="2" ry="1.5"/><ellipse cx="11" cy="7.5" rx="2" ry="1.5"/></svg>Blue Tern - 7pm</li>
        <li class="act"><svg class="note" viewBox="0 0 14 11"><path d="M5 9V2l8-1.5V7.5M5 3.5l8-1.5"/><ellipse cx="3" cy="9" rx="2" ry="1.5"/><ellipse cx="11" cy="7.5" rx="2" ry="1.5"/></svg>Velvet Kite &amp; Slow Morris - 3pm - 7pm</li>
        <li class="act"><svg class="note" viewBox="0 0 14 11"><path d="M5 9V2l8-1.5V7.5M5 3.5l8-1.5"/><ellipse cx="3" cy="9" rx="2" ry="1.5"/><ellipse cx="11" cy="7.5" rx="2" ry="1.5"/></svg>Grant Whitcombe - 12pm - 3pm</li>
      </ul>
    </div>
  </div>
</section>

</body>
</html>
```